practice letterhead

I need a letterhead design for a new company that is a veterinary specialty company. I am conservative. I want it to look professional - not "cutesy"

I need my name, credentials, address, phone number and website/email on it.

My personal information is as follows: Lorraine Aldous, DVM, DACVIM (Neurology) Certified Veterinary Pain Practitioner (or CVPP) Certified Canine Rehabilitation Therapist (or CCRT) 1487 Marden Hwy Marden Falls, CT 06417 860-374-6620 lorraine.aldous@kindpawspecialty.com www.kindpawspecialty.com

```html
<!DOCTYPE html>
<html lang="en">
<head>
<meta charset="utf-8">
<title>Kind Paw Veterinary Specialty Center — Letterhead</title>
<link href="https://fonts.googleapis.com/css2?family=Arimo:wght@400;700&display=swap" rel="stylesheet">
<style>
  :root {
    --teal: #6e9588;
    --mauve: #9a6c79;
    --mauve-light: #b7969d;
    --mauve-dark: #6e4c58;
    --ink: #1f1f1f;
    --paper: #ffffff;
  }
  * { margin: 0; padding: 0; box-sizing: border-box; }
  html, body { width: 848px; height: 1200px; overflow: hidden; background: var(--paper); }
  .letterhead {
    position: relative;
    width: 848px;
    height: 1200px;
    background: var(--paper);
    font-family: "Arimo", Arial, sans-serif;
    color: var(--ink);
  }
  .frame { position: absolute; inset: 0; }
  .brand {
    position: absolute;
    top: 150px;
    left: 0;
    width: 848px;
    display: flex;
    justify-content: center;
    align-items: center;
    gap: 10px;
  }
  .brand-dot {
    width: 34px; height: 34px;
    border-radius: 50%;
    background: var(--teal);
    flex: none;
  }
  .brand-name {
    font-weight: 700;
    font-size: 15px;
    line-height: 17px;
    color: var(--teal);
    letter-spacing: 0.2px;
  }
  .letter-body {
    position: absolute;
    left: 137px;
    top: 258px;
    width: 576px;
    font-size: 16px;
    line-height: 25.4px;
  }
  .letter-body p { margin-bottom: 25.4px; }
  .line { display: block; white-space: nowrap; text-align: justify; text-align-last: justify; }
  .line-end { display: block; white-space: nowrap; text-align: left; }
  .signature {
    position: absolute;
    right: 15px;
    top: 983px;
    width: 600px;
    text-align: right;
    font-size: 16px;
    line-height: 19.5px;
    color: var(--mauve);
  }
</style>
</head>
<body>
<div class="letterhead">
  <svg class="frame" width="848" height="1200" viewBox="0 0 848 1200" aria-hidden="true">
    <path d="M0 0 H848 V150 H615 A210 105 0 0 0 245 150 H0 Z" fill="var(--teal)"/>
    <polygon points="0,159 218,159 210,167 0,167" fill="var(--mauve)"/>
    <polygon points="630,159 848,159 848,167 638,167" fill="var(--mauve)"/>

    <rect x="16" y="179" width="30" height="29" fill="var(--mauve)"/>
    <rect x="54" y="179" width="30" height="29" fill="var(--mauve-light)"/>
    <rect x="16" y="216" width="30" height="29" fill="var(--mauve-dark)"/>

    <rect x="767" y="179" width="30" height="29" fill="var(--mauve-light)"/>
    <rect x="805" y="179" width="30" height="29" fill="var(--mauve)"/>
    <rect x="805" y="216" width="30" height="29" fill="var(--mauve-dark)"/>

    <rect x="100" y="180" width="1.5" height="918" fill="var(--mauve)"/>
    <rect x="746" y="180" width="1.5" height="795" fill="var(--mauve)"/>

    <rect x="16" y="1030" width="30" height="29" fill="var(--mauve-dark)"/>
    <rect x="16" y="1067" width="30" height="29" fill="var(--mauve)"/>
    <rect x="54" y="1067" width="30" height="29" fill="var(--mauve-light)"/>

    <rect x="0" y="1107" width="848" height="8" fill="var(--mauve)"/>
    <rect x="0" y="1124" width="848" height="76" fill="var(--teal)"/>
  </svg>

  <header class="brand">
    <span class="brand-dot"></span>
    <span class="brand-name">Kind Paw Veterinary<br>Specialty Center</span>
  </header>

  <main class="letter-body">
    <p><span class="line-end">Lorem Ipsum,</span></p>
    <p>
      <span class="line">Lorem ipsum dolor sit amet, consectetur adipiscing elit. Maecenas</span>
      <span class="line">ullamcorper laoreet augue, vel eleifend tellus eleifend sed. Phasellus in</span>
      <span class="line">posuere mi. Mauris vitae vulputate erat. Integer quis facilisis dui. Nunc aliquam</span>
      <span class="line">posuere turpis id venenatis. Donec bibendum vel augue et cursus. Fusce</span>
      <span class="line-end">egestas malesuada dictum.</span>
    </p>
    <p>
      <span class="line">Ut augue sem, lacinia id arcu vel, fringilla sodales sem. Pellentesque</span>
      <span class="line">pellentesque dui erat, at vulputate mauris blandit id. Sed euismod sit amet</span>
      <span class="line">lacus ut dictum. Vivamus malesuada sodales enim, id tristique turpis faucibus</span>
      <span class="line">vel. Maecenas vitae dapibus sem. Maecenas dui tortor, tincidunt id lobortis</span>
      <span class="line">non, fringilla in elit. Phasellus cursus urna sed hendrerit luctus. Pellentesque</span>
      <span class="line">tempus urna sed nibh suscipit, sed iaculis leo malesuada. Nam tellus purus,</span>
      <span class="line-end">sagittis ac sodales sit amet, suscipit non massa.</span>
    </p>
    <p>
      <span class="line">Mauris ac vestibulum nisi. Donec molestie dignissim dui, at tristique eros. Sed</span>
      <span class="line">elit enim, mattis quis odio in, congue ultrices tellus. Nam feugiat massa vel dui</span>
      <span class="line">rhoncus tristique. Vestibulum tempor velit dignissim, volutpat magna nec,</span>
      <span class="line">scelerisque nisi. Mauris tellus leo, interdum id urna eget, rhoncus fringilla</span>
      <span class="line">tellus. Sed ut ultricies augue. Donec faucibus mi sit amet dui rhoncus, eu</span>
      <span class="line">placerat ipsum aliquet. Donec gravida tristique massa id rutrum. Fusce non</span>
      <span class="line-end">malesuada sapien. In varius metus laoreet, iaculis tortor ultrices, viverra ante.</span>
    </p>
    <p>
      <span class="line">Quisque vel pharetra odio. Aliquam euismod auctor commodo. Aliquam nec</span>
      <span class="line-end">justo ut sem dictum ullamcorper quis eu sem.</span>
    </p>
  </main>

  <footer class="signature">
    Lorraine Aldous, DVM, Board-Certified Veterinary Neurologist, Certified<br>
    Pain and Rehabilitation Practitioner<br>
    1487 Marden Hwy Marden Falls, CT;<br>
    06417 860-374-6620<br>
    lorraine.aldous@kindpawspecialty.com<br>
    www.kindpawspecialty.com
  </footer>
</div>
</body>
</html>
```